Business Card

I would like a business card with a picture of my husband and I that is unique and professional.

Industry/Entity Type

Business

Font styles to use
Serif

```html
<!DOCTYPE html>
<html lang="en">
<head>
<meta charset="utf-8">
<title>Marlo Beckett — Business Card</title>
<link rel="stylesheet" href="https://fonts.googleapis.com/css2?family=Della+Respira&display=swap">
<style>
  :root {
    --card-bg: #ffffff;
    --band-charcoal: #555555;
    --band-yellow: #fedc45;
    --ink: #111111;
  }
  * { margin: 0; padding: 0; box-sizing: border-box; }
  html, body {
    width: 1200px;
    height: 700px;
    overflow: hidden;
    background: var(--card-bg);
  }
  .card {
    position: relative;
    width: 1200px;
    height: 700px;
    background: var(--card-bg);
  }
  .card__arc {
    position: absolute;
    inset: 0;
  }
  .card__arc .band--charcoal { fill: var(--band-charcoal); }
  .card__arc .band--yellow { fill: var(--band-yellow); }
  .contact {
    position: absolute;
    left: 477px;
    top: 224px;
    font-family: "Della Respira", serif;
    color: var(--ink);
    font-size: 44px;
    line-height: 64.5px;
    letter-spacing: 0.5px;
    white-space: nowrap;
  }
  .contact__line { display: block; }
</style>
</head>
<body>
  <main class="card">
    <svg class="card__arc" width="1200" height="700" viewBox="0 0 1200 700" aria-hidden="true">
      <defs>
        <filter id="arc-shadow" x="-20%" y="-5%" width="140%" height="110%">
          <feDropShadow dx="-3" dy="0" stdDeviation="3" flood-color="#000" flood-opacity="0.35"/>
        </filter>
      </defs>
      <g filter="url(#arc-shadow)">
        <path class="band--charcoal" d="M278 0 Q425 350 276 700 L323 700 Q505 350 323 0 Z"/>
        <path class="band--yellow" d="M323 0 Q505 350 323 700 L368 700 Q549 350 362 0 Z"/>
      </g>
    </svg>
    <div class="contact">
      <span class="contact__line contact__name">Marlo Beckett</span>
      <span class="contact__line contact__title">Professional Mentorship Strategist</span>
      <span class="contact__line contact__phone">312-555-0148</span>
      <span class="contact__line contact__email">HelloMarloBeckett@inbox.net</span>
    </div>
  </main>
</body>
</html>
```